GUARANTEED! Simple website for independent event planner and consultant...

I need a website that is no more than 5 or 6 pages to illustrate who I am and what I can offer to groups who book hotels for meetings and conferences. I have 20 years of experience planning meetings within hotels and I am now ready to go out on my own and help clients choose venues, negotiate contracts and plan effective meetings. I will focus on clients planning meetings in the mountains of Colorado but I am willing to travel as well. I want to work with a person who is collaborative and can direct me on what they need to move the project along quickly. I already have my logo, a hosting site and work e-mail address. Also, I recently hired a photographer to do head shots. Lastly, it important for me to be able to talk on the phone or skype with this person, as needed and I must be able to make changes to my site down the road when necessary...

Target Market(s)

Corporate Groups

Industry/Entity Type

Event Planning

Coding

Coded - Design and coding required

Number of Pages Required

5+ page

Font styles to use
Sans Serif

Requirements
Must have
• About me page, event planning services offered page, task force and consulting work page, testimonials page, page for blogs, page to contact me/request a proposal. May need advice on what else I need...
Nice to have
• I want it to look sharp and professional. I want people to look at my site and know immediately that they can trust me and the work I can do.
• I don't want it to look like it is over the top as I am not a HUGE company but I do want it to be professional and easy to view and navigate.
Should not have
• Bright colors
• My logo is bright orange and black. I have also used dark grey and orange. See below:
• Orange:
• C = 0
• M = 64
• Y = 100
• K = 0
• Gray:
• C = 67
• M = 60
• Y = 59
• K = 45
• Font: Gotham Book and Gotham Bold

```html
<!DOCTYPE html>
<html lang="en">
<head>
<meta charset="utf-8">
<title>Halden Event Management</title>
<link href="https://fonts.googleapis.com/css2?family=Zilla+Slab:wght@300;400;600;700&family=Roboto:wght@400;500;700&display=swap" rel="stylesheet">
<style>
:root{
  --orange:#f15a24;
  --ink:#3a3a3a;
  --text:#6b6b6b;
  --muted:#8a8a8a;
  --paper:#fafafa;
  --band:#f2f1ef;
  --card:#ffffff;
  --line:#e6e4e1;
}
*{box-sizing:border-box;margin:0;padding:0}
html,body{width:1200px;height:3352px;overflow:hidden}
body{background:var(--paper);font-family:"Roboto",Arial,sans-serif;color:var(--text);font-size:11px;line-height:1.45}
a{color:var(--orange);text-decoration:none}
.wrap{width:850px;margin:0 auto;position:relative}
.more{font-size:11px;color:var(--orange);display:inline-flex;align-items:center;gap:5px}
.more .arrow{width:6px;height:8px;flex:none}
h1,h2,h3,blockquote,.brand{font-family:"Zilla Slab",Georgia,serif}

/* header */
.site-header{height:108px;border-bottom:1px solid var(--line);width:850px;margin:0 auto;display:flex;align-items:center}
.brand{font-size:22px;font-weight:700;color:var(--orange);width:125px}
.main-nav{display:flex;gap:22px;font-size:11.5px;color:var(--ink)}
.social{margin-left:auto;display:flex;gap:9px;margin-right:44px}
.social span{width:10px;height:10px;border-radius:50%;background:var(--ink)}
.cta{background:var(--orange);color:#fff;font-size:11.5px;font-weight:500;width:146px;height:36px;display:flex;align-items:center;justify-content:center}

/* hero */
.hero{height:428px;padding-top:112px}
.hero h1{font-weight:300;font-size:35px;line-height:1.27;color:var(--ink);width:620px}
.hero h1 .name{color:var(--orange);text-decoration:underline;text-decoration-thickness:1px;text-underline-offset:4px}
.hero p{font-size:13px;width:580px;margin:14px 0 12px;line-height:1.45}

/* services */
.services{background:var(--band);height:578px;padding-top:74px;text-align:center}
.section-title{font-size:24px;font-weight:600;color:var(--ink)}
.section-lede{font-size:12px;width:460px;margin:14px auto 12px;line-height:1.35}
.service-grid{display:flex;gap:30px;margin-top:44px}
.service-card{width:190px;height:234px;background:var(--card);box-shadow:0 1px 3px rgba(0,0,0,.06);padding-top:28px}
.service-card .icon{width:66px;height:66px;stroke:var(--muted);fill:none;stroke-width:1.6}
.service-card h3{font-size:13px;font-weight:700;color:var(--ink);margin:18px 0 4px}
.service-card p{font-size:10.5px;line-height:1.3;width:150px;margin:0 auto 10px}

/* statement */
.statement{display:flex;height:430px;margin-top:62px;background:#fff}
.statement .photo{width:592px;height:430px;margin-left:7px;background:linear-gradient(90deg,#8c4a32 0%,#b06444 45%,#d9d4cc 75%,#f1efeb 100%)}
.statement .body{padding:60px 0 0 90px}
.statement blockquote{font-size:31px;font-weight:300;line-height:1.32;color:var(--ink);width:310px;margin-bottom:18px}
.person{display:flex;align-items:center;gap:16px;margin-top:26px}
.avatar{width:58px;height:58px;border-radius:50%;background:linear-gradient(135deg,#e7d6c8,#c8a88f)}
.person b{display:block;font-family:"Zilla Slab",Georgia,serif;font-size:12px;color:var(--ink)}
.person small{font-size:10.5px}

/* insights */
.insights{height:1128px;padding-top:94px;text-align:center}
.post-grid{display:flex;gap:39px;margin-top:60px;text-align:left}
.post-col{width:257px;display:flex;flex-direction:column;gap:33px}
.post{background:var(--card);box-shadow:0 1px 3px rgba(0,0,0,.06)}
.post .img{width:100%}
.post .copy{padding:24px 24px 26px}
.post h3{font-size:16px;font-weight:700;color:var(--ink);line-height:1.25;margin-bottom:10px}
.post p{font-size:10.5px;line-height:1.35;margin-bottom:14px}
.g1{background:linear-gradient(135deg,#6b5a4d,#b7a28e)}
.g2{background:linear-gradient(135deg,#1c1f2a,#4a3e3a)}
.g3{background:linear-gradient(180deg,#2a2a2e,#c9c6c2)}
.g4{background:linear-gradient(135deg,#8a7b70,#c9c3bb)}
.g5{background:linear-gradient(135deg,#3a3530,#d3b682)}
.g6{background:linear-gradient(135deg,#1d1d1d,#5e5a57)}

/* testimonial */
.testimonial{background:var(--band);height:410px;text-align:center;padding-top:62px}
.testimonial .intro{font-size:12px;width:400px;margin:0 auto 24px;line-height:1.4}
.testimonial blockquote{font-size:29px;font-weight:300;line-height:1.3;color:var(--ink);width:760px;margin:0 auto}
.testimonial .person{justify-content:center;text-align:left;margin-top:22px}
.dots{display:flex;gap:5px;justify-content:center;margin-top:34px}
.dots span{width:5px;height:5px;border-radius:50%;background:#cfcdca}
.dots span:first-child{background:var(--ink)}

/* footer */
.site-footer{height:272px;padding-top:58px}
.footer-cols{display:flex}
.footer-about{width:255px}
.footer-about .brand{display:block;margin-bottom:14px}
.footer-about p{font-size:10.5px;width:175px;line-height:1.35;color:var(--ink)}
.footer-col{width:160px;font-size:11px;line-height:1.4}
.footer-col:last-child{width:auto}
.footer-col h4{font-family:"Zilla Slab",Georgia,serif;font-size:12px;color:var(--ink);font-weight:700;margin-bottom:8px}
.footer-col .social{margin:6px 0 0;gap:6px}
.footer-col .social span{width:9px;height:9px}
.legal{border-top:1px solid var(--line);margin-top:60px;padding-top:14px;font-size:10px;color:var(--ink);display:flex;gap:12px}
</style>
</head>
<body>

<header class="site-header">
  <span class="brand">Halden</span>
  <nav class="main-nav">
    <span>About</span><span>Services</span><span>Customers</span><span>Thoughts &amp; Insights</span><span>Contact</span>
  </nav>
  <div class="social" aria-label="Social links"><span></span><span></span><span></span></div>
  <a class="cta" href="#">Let's work together</a>
</header>

<section class="hero">
  <div class="wrap">
    <h1>I'm <span class="name">Mara Ellison</span>, an event planner &amp; consultant based in the city of Grand Junction, Colorado.</h1>
    <p>I focus on providing as much or as little support as my clients need on all aspects of their event. Honesty, integrity and loyalty are my watchwords.</p>
    <a class="more" href="#">Know more <svg class="arrow" viewBox="0 0 6 8"><path d="M1 1l3 3-3 3" stroke="currentColor" fill="none" stroke-width="1.4"/></svg></a>
  </div>
</section>

<section class="services">
  <div class="wrap">
    <h2 class="section-title">Services &amp; Offers</h2>
    <p class="section-lede">We offer quality consulting &amp; events planning services and we are growing to offer a wide panel of complementary offers for our customers.</p>
    <a class="more" href="#">Know more <svg class="arrow" viewBox="0 0 6 8"><path d="M1 1l3 3-3 3" stroke="currentColor" fill="none" stroke-width="1.4"/></svg></a>
    <div class="service-grid">
      <div class="service-card">
        <svg class="icon" viewBox="0 0 66 66"><rect x="24" y="6" width="22" height="14" rx="2"/><circle cx="20" cy="34" r="6"/><circle cx="46" cy="34" r="6"/><path d="M8 58c0-10 6-14 12-14s12 4 12 14M34 58c0-10 6-14 12-14s12 4 12 14"/></svg>
        <h3>Consulting &amp; Task Force</h3>
        <p>It was shaped like a chair spark with gems, as did everything.</p>
        <a class="more" href="#">Know more <svg class="arrow" viewBox="0 0 6 8"><path d="M1 1l3 3-3 3" stroke="currentColor" fill="none" stroke-width="1.4"/></svg></a>
      </div>
      <div class="service-card">
        <svg class="icon" viewBox="0 0 66 66"><path d="M8 58h50M12 58V20M54 58V20M12 20h42"/><path d="M24 58V40h18v18M22 32l11-8 11 8"/></svg>
        <h3>Social Events Planning</h3>
        <p>It was shaped like a chair spark with gems, as did everything.</p>
        <a class="more" href="#">Know more <svg class="arrow" viewBox="0 0 6 8"><path d="M1 1l3 3-3 3" stroke="currentColor" fill="none" stroke-width="1.4"/></svg></a>
      </div>
      <div class="service-card">
        <svg class="icon" viewBox="0 0 66 66"><rect x="20" y="8" width="26" height="50"/><rect x="8" y="28" width="12" height="30"/><rect x="46" y="22" width="12" height="36"/><path d="M26 16h4M36 16h4M26 26h4M36 26h4M26 36h4M36 36h4M26 46h4M36 46h4"/></svg>
        <h3>Business Events Planning</h3>
        <p>It was shaped like a chair spark with gems, as did everything.</p>
        <a class="more" href="#">Know more <svg class="arrow" viewBox="0 0 6 8"><path d="M1 1l3 3-3 3" stroke="currentColor" fill="none" stroke-width="1.4"/></svg></a>
      </div>
      <div class="service-card">
        <svg class="icon" viewBox="0 0 66 66"><circle cx="33" cy="14" r="5"/><circle cx="16" cy="36" r="5"/><circle cx="33" cy="36" r="5"/><circle cx="50" cy="36" r="5"/><path d="M25 28c0-4 4-6 8-6s8 2 8 6M8 52c0-5 4-8 8-8s8 3 8 8M25 52c0-5 4-8 8-8s8 3 8 8M42 52c0-5 4-8 8-8s8 3 8 8"/></svg>
        <h3>Public &amp; Open Planning</h3>
        <p>It was shaped like a chair spark with gems, as did everything.</p>
        <a class="more" href="#">Know more <svg class="arrow" viewBox="0 0 6 8"><path d="M1 1l3 3-3 3" stroke="currentColor" fill="none" stroke-width="1.4"/></svg></a>
      </div>
    </div>
  </div>
</section>

<section class="statement">
  <div class="photo" role="img" aria-label="Meeting room with a brick wall, a long white table and black chairs"></div>
  <div class="body">
    <blockquote>“I am convinced that when you have the right partner, the process can be surprisingly simple.”</blockquote>
    <a class="more" href="#">More About Halden <svg class="arrow" viewBox="0 0 6 8"><path d="M1 1l3 3-3 3" stroke="currentColor" fill="none" stroke-width="1.4"/></svg></a>
    <div class="person">
      <div class="avatar" role="img" aria-label="Portrait of Mara Ellison"></div>
      <div><b>Mara Ellison</b><small>Manager at Halden Event Management</small></div>
    </div>
  </div>
</section>

<section class="insights">
  <div class="wrap">
    <h2 class="section-title">Thoughts &amp; Insights</h2>
    <p class="section-lede">Company news, articles, blogs and events to share our expertise and keep you up to date with what is happening at Halden Event Management.</p>
    <a class="more" href="#">Discover the Blog <svg class="arrow" viewBox="0 0 6 8"><path d="M1 1l3 3-3 3" stroke="currentColor" fill="none" stroke-width="1.4"/></svg></a>
    <div class="post-grid">
      <div class="post-col">
        <article class="post"><div class="img g1" style="height:118px" role="img" aria-label="Crowd of festival visitors seen from behind"></div>
          <div class="copy"><h3>All speaking her delicate reccured possible at</h3><p>It was shaped like a chair sparkled with gems, as did everything else. In the center of the chair was an enormous Head, without a body to support it or any arms or legs whatever.</p><a class="more" href="#">Read more <svg class="arrow" viewBox="0 0 6 8"><path d="M1 1l3 3-3 3" stroke="currentColor" fill="none" stroke-width="1.4"/></svg></a></div></article>
        <article class="post"><div class="img g4" style="height:237px" role="img" aria-label="Person packing a parcel on a table"></div>
          <div class="copy"><h3>All speaking her delicate reccured possible at</h3><p>It was shaped like a chair sparkled with gems, as did everything else. In the center of the chair was an enormous Head, without a body to support it or any arms or legs whatever.</p><a class="more" href="#">Read more <svg class="arrow" viewBox="0 0 6 8"><path d="M1 1l3 3-3 3" stroke="currentColor" fill="none" stroke-width="1.4"/></svg></a></div></article>
      </div>
      <div class="post-col">
        <article class="post"><div class="img g2" style="height:239px" role="img" aria-label="Concert crowd with raised hands under stage lights"></div>
          <div class="copy"><h3>All speaking her delicate reccured possible at</h3><p>It was shaped like a chair sparkled with gems, as did everything else. In the center of the chair was an enormous Head, without a body to support it or any arms or legs whatever.</p><a class="more" href="#">Read more <svg class="arrow" viewBox="0 0 6 8"><path d="M1 1l3 3-3 3" stroke="currentColor" fill="none" stroke-width="1.4"/></svg></a></div></article>
        <article class="post"><div class="img g5" style="height:118px" role="img" aria-label="Conference hall with screens and attendees"></div>
          <div class="copy"><h3>All speaking her delicate reccured possible at</h3><p>It was shaped like a chair sparkled with gems, as did everything else. In the center of the chair was an enormous Head, without a body to support it or any arms or legs whatever.</p><a class="more" href="#">Read more <svg class="arrow" viewBox="0 0 6 8"><path d="M1 1l3 3-3 3" stroke="currentColor" fill="none" stroke-width="1.4"/></svg></a></div></article>
      </div>
      <div class="post-col">
        <article class="post"><div class="img g3" style="height:118px" role="img" aria-label="Fashion show runway with models"></div>
          <div class="copy"><h3>All speaking her delicate reccured possible at</h3><p>It was shaped like a chair sparkled with gems, as did everything else. In the center of the chair was an enormous Head, without a body to support it or any arms or legs whatever.</p><a class="more" href="#">Read more <svg class="arrow" viewBox="0 0 6 8"><path d="M1 1l3 3-3 3" stroke="currentColor" fill="none" stroke-width="1.4"/></svg></a></div></article>
        <article class="post"><div class="img g6" style="height:237px" role="img" aria-label="Visitor looking at an artwork in a gallery"></div>
          <div class="copy"><h3>All speaking her delicate reccured possible at</h3><p>It was shaped like a chair sparkled with gems, as did everything else. In the center of the chair was an enormous Head, without a body to support it or any arms or legs whatever.</p><a class="more" href="#">Read more <svg class="arrow" viewBox="0 0 6 8"><path d="M1 1l3 3-3 3" stroke="currentColor" fill="none" stroke-width="1.4"/></svg></a></div></article>
      </div>
    </div>
  </div>
</section>

<section class="testimonial">
  <p class="intro">Don't take it just form me, discover what my clients have to say about Halden Events Management Services, people and expertise.</p>
  <blockquote>“I had the opportunity to collaborate with Mara at the Summit Forum in March. What a treat! She is very profesional, creative and full of energy.</blockquote>
  <div class="person">
    <div class="avatar" role="img" aria-label="Portrait of Lena Marchetti"></div>
    <div><b>Lena Marchetti</b><small>Author, New York City</small></div>
  </div>
  <div class="dots"><span></span><span></span><span></span><span></span></div>
</section>

<footer class="site-footer">
  <div class="wrap">
    <div class="footer-cols">
      <div class="footer-about">
        <span class="brand">Halden</span>
        <p>Lorem ipsum dolor sit amet, consectetur adipisicing elit, sed do eiusmod tempor incididunt ut labore et dolore magna aliqua. Ut enim ad le dolore magna aliquam quaerat voluptatem.</p>
      </div>
      <div class="footer-col"><h4>Services</h4>Consulting &amp; Task Force<br>Social Events<br>Corporate Events</div>
      <div class="footer-col" style="width:145px"><h4>Clients</h4>Testimonials<br>Case Studies<br>Resources</div>
      <div class="footer-col" style="width:105px"><h4>Company</h4>About<br>Partners<br>Blog</div>
      <div class="footer-col"><h4>Get in touch</h4>Contact<br>Social<div class="social"><span></span><span></span><span></span></div></div>
    </div>
    <div class="legal"><span>© 2017 Halden Event Management</span><span>Legal Terms</span><span>Credits</span><span>Sitemap</span></div>
  </div>
</footer>

</body>
</html>
```